依頼概要
■依頼の目的/概要
大型施設の共有スペースに展示する商品のPOPのデザインをお願いします。
展示の全体イメージがありますのでそれに合わせたイメージで制作して下さい。

■依頼詳細
大型SC内の新店舗の商品展示用のPOPになります。
展示イメージに合うようにPOPの制作をして下さい。
前回の展示のPOPを参考にアップしておきますが、同じような配置にする必要はございません。
前回は背景色などは変えずに、商品名、金額等を、レディース、メンズ、キッズの三種類に色分けして区別しておりました。
今回はキッズはないのですが、レディース、メンズ、雑貨と別れておりますので、うまく区別できるような工夫をお願いします。
サイズは A4縦サイズ。
店舗によって商品、金額、アイテム数は変化するので、変更できるような仕様にして下さい。
フォントはモリサワでしたら入っております。
採用後は使用フォントを納品データと共にお知らせください。

■重視する点
Illustrator・Photoshopの経験必須でお願いします。
新店舗のPOPになりますので、」お客様の目に留まるようなデザインが望ましいです。

■継続依頼について
弊社ではこういった案件が多くあり、次回は母の日、父の日等もありますので、継続的依頼できるありがたいです。

その他何かご不明な点がございましたら、お気軽にご質問下さい。
よろしくお願いいたします。
参考用イメージをアップします。

今回の展示イメージ
前回のPOPイメージ

の2点です。
1店舗の最大アイテム数は6になります。
前回のPOP参考例はあくまで参考です。
同じように作作らなくても良いので参考程度にして頂ければ幸いです。
展示イメージにある通り、POPは各マネキン、雑貨の前に置くものになります。
新店舗のオープンなのでワクワクするようなイメージで制作してもらえればと思います。
集まりが少ないので当選額を上乗せします。
それに伴い期間も延長いたします。
ご応募いただきありがとうございました。

見やすくイメージに沿っていたため。

たくさんのご参加ありがとうございました。
ぜひ次回もご参加下さい。

```html
<!DOCTYPE html>
<html lang="ja">
<head>
<meta charset="UTF-8">
<title>NEW ITEMS POP</title>
<link href="https://fonts.googleapis.com/css2?family=Luckiest+Guy&family=M+PLUS+Rounded+1c:wght@500;700;800&display=swap" rel="stylesheet">
<style>
  :root {
    --cork-light: #d4ad82;
    --cork-dark: #b98c5e;
    --paper-white: #f6f4ef;
    --paper-pink: #f2c4c6;
    --card-white: #ffffff;
    --card-pink: #fde6e6;
    --ladies: #e8558a;
    --goods: #f0c02c;
    --mens: #3db3df;
    --price: #e2457e;
    --ink: #3a2c25;
    --title: #6a4227;
    --tape-blue: #8fd0ea;
    --tape-pink: #f5a3bd;
    --tape-yellow: #f7dc6a;
    --daisy-tone: #f7f3e8;
    --daisy-shade: #e9dfc6;
    --berry-tone: #d9394a;
    --berry-shade: #b62a38;
  }
  * { margin: 0; padding: 0; box-sizing: border-box; }
  html, body { width: 849px; height: 1200px; overflow: hidden; }
  body { font-family: "M PLUS Rounded 1c", sans-serif; color: var(--ink); }
  .pop {
    position: relative; width: 849px; height: 1200px; overflow: hidden;
    background: radial-gradient(circle at 40% 35%, var(--cork-light), var(--cork-dark));
  }
  .title {
    position: absolute; left: 350px; top: 22px; white-space: nowrap;
    font-family: "Luckiest Guy", sans-serif; font-size: 82px; font-weight: 400; color: var(--title);
    line-height: 1;
    text-shadow: 4px 0 #fff, -4px 0 #fff, 0 4px #fff, 0 -4px #fff, 3px 3px #fff, -3px -3px #fff, 3px -3px #fff, -3px 3px #fff;
    transform: rotate(-2deg);
  }
  .daisy-art {
    position: absolute; border-radius: 18px;
    background: radial-gradient(circle at 50% 45%, var(--daisy-tone), var(--daisy-shade));
    opacity: .9;
  }
  .berry-art {
    position: absolute; border-radius: 18px;
    background: linear-gradient(160deg, var(--berry-tone), var(--berry-shade));
  }
  .board {
    position: absolute; width: 595px; height: 285px;
    box-shadow: 3px 4px 8px rgba(0,0,0,.25);
  }
  .board.white { background: var(--paper-white); }
  .board.pink { background: var(--paper-pink); }
  .card {
    position: absolute; width: 552px; height: 118px; background: var(--card-white);
    box-shadow: 2px 3px 5px rgba(0,0,0,.2);
  }
  .card.soft { background: var(--card-pink); }
  .tag {
    position: absolute; left: 22px; top: 12px; padding: 1px 14px;
    font-size: 19px; font-weight: 700; color: #fff; border-radius: 3px;
  }
  .tag.ladies { background: var(--ladies); }
  .tag.goods { background: var(--goods); }
  .tag.mens { background: var(--mens); }
  .name { position: absolute; left: 22px; top: 42px; font-size: 46px; font-weight: 700; white-space: nowrap; }
  .price { position: absolute; left: 300px; top: 4px; font-size: 60px; font-weight: 800; color: var(--price); white-space: nowrap; }
  .tax { position: absolute; left: 370px; top: 82px; font-size: 21px; font-weight: 500; white-space: nowrap; }
  .tape { position: absolute; width: 90px; height: 26px; opacity: .9; }
  .tape.blue { background: var(--tape-blue); }
  .tape.pink { background: var(--tape-pink); }
  .tape.yellow { background: var(--tape-yellow); }
  .footer {
    position: absolute; left: 28px; top: 1035px; width: 793px; height: 148px;
    background: #fff; border: 10px solid var(--ladies);
  }
  .shop-logo { position: absolute; left: 42px; top: 46px; font-size: 30px; font-weight: 700; }
  .divider { position: absolute; left: 195px; top: 14px; width: 3px; height: 100px; background: var(--ladies); }
  .floor {
    position: absolute; left: 232px; top: 28px; width: 66px; height: 66px; border-radius: 50%;
    background: var(--ladies); color: #fff; font-size: 26px; font-weight: 800;
    display: flex; align-items: center; justify-content: center;
  }
  .shop-name { position: absolute; left: 318px; top: 30px; font-size: 46px; font-weight: 800; }
  .corp-logo { position: absolute; right: 30px; bottom: 10px; font-size: 22px; font-weight: 500; }
</style>
</head>
<body>
<main class="pop">
  <div class="daisy-art" style="left:250px;top:12px;width:86px;height:86px;" role="img" aria-label="白いデイジーの花のイラスト"></div>
  <h1 class="title">NEW ITEMS</h1>

  <section class="board white" style="left:127px;top:152px;transform:rotate(-1deg);">
    <div class="card" style="left:26px;top:20px;">
      <span class="tag ladies">Ladies'</span><span class="name">ジャケット</span>
      <span class="price">¥5,900</span><span class="tax">(税込 ¥6,372)</span>
    </div>
    <div class="card" style="left:26px;top:152px;">
      <span class="tag ladies">Ladies'</span><span class="name">スカート</span>
      <span class="price">¥4,900</span><span class="tax">(税込 ¥5,292)</span>
    </div>
  </section>
  <div class="tape blue" style="left:95px;top:150px;transform:rotate(-30deg);"></div>
  <div class="tape blue" style="left:660px;top:150px;transform:rotate(25deg);"></div>

  <section class="board pink" style="left:228px;top:458px;transform:rotate(1deg);">
    <div class="card soft" style="left:22px;top:18px;">
      <span class="tag ladies">Ladies'</span><span class="name">ブラウス</span>
      <span class="price">¥4,200</span><span class="tax">(税込 ¥4,536)</span>
    </div>
    <div class="card soft" style="left:22px;top:148px;">
      <span class="tag goods">Goods</span><span class="name">パンプス</span>
      <span class="price">¥3,800</span><span class="tax">(税込 ¥4,104)</span>
    </div>
  </section>
  <div class="tape pink" style="left:200px;top:462px;transform:rotate(-25deg);"></div>
  <div class="tape yellow" style="left:760px;top:455px;transform:rotate(30deg);"></div>

  <section class="board white" style="left:113px;top:750px;transform:rotate(-1deg);">
    <div class="card" style="left:22px;top:18px;">
      <span class="tag mens">Men's</span><span class="name">ジャケット</span>
      <span class="price">¥5,900</span><span class="tax">(税込 ¥6,372)</span>
    </div>
    <div class="card" style="left:22px;top:148px;">
      <span class="tag mens">Men's</span><span class="name">セーター</span>
      <span class="price">¥5,900</span><span class="tax">(税込 ¥6,372)</span>
    </div>
  </section>
  <div class="tape blue" style="left:80px;top:755px;transform:rotate(-28deg);"></div>
  <div class="berry-art" style="left:712px;top:880px;width:74px;height:80px;" role="img" aria-label="いちごのイラスト"></div>
  <div class="daisy-art" style="left:724px;top:968px;width:76px;height:62px;" role="img" aria-label="白いデイジーの花のイラスト"></div>

  <footer class="footer">
    <span class="shop-logo">店舗ロゴ</span>
    <span class="divider"></span>
    <span class="floor">2階</span>
    <span class="shop-name">店舗名</span>
    <span class="corp-logo">コーポレートロゴ</span>
  </footer>
</main>
</body>
</html>
```